Business Cards for Branding (Advertising) Agency

We need stylish and cool business cards.
Additional info:
1) Logo - see the attachment. You can use either the three penguins or just one penguin face (square or round) - at your discretion.
2) Text and other stuff for business card:
front side:
-Logo and company name: company name - Northern Herons - should be in English as is in logo. This is the only exception. The rest of the text will be in Russian.
-Who we are: Брендинговое агентство
-First and last name:
-Position: Управляющий партнёр
-Address:
-Phone:
-Email:
-Website:
Note: please don't use names of information fields, such as: who we are, first and last name, position, address, phone, email and website.

3) Our suggestions on design:
-The backside of the business card can be either blank or has something on it - at your discretion.
-The business card background should be either white or grey (you can use any tone of grey).

Additional Information:
1) БРЕНДИНГОВОЕ АГЕНТСТВО
2) ул. Верескова - these two words should be together on the same line
3) тел.: +7 (495) 381-60-92
моб.: +7 (916) 507-28-14

Reason: We would like to receive more stylish designs.

```html
<!DOCTYPE html>
<html lang="ru">
<head>
<meta charset="utf-8">
<title>Northern Herons — визитная карточка</title>
<link rel="stylesheet" href="https://fonts.googleapis.com/css2?family=Roboto:wght@300;400;500&display=swap">
<style>
  :root {
    --bg: #e4e1dc;
    --card: #ffffff;
    --ink: #1a1a1a;
    --grey: #8a8a8a;
    --grey-dark: #555555;
    --orange: #f29d12;
    --rule: #d6d6d6;
  }
  * { box-sizing: border-box; margin: 0; padding: 0; }
  html, body { width: 1200px; height: 1000px; overflow: hidden; }
  body {
    background: var(--bg);
    font-family: "Roboto", Arial, sans-serif;
    position: relative;
  }
  .card {
    position: absolute;
    background: var(--card);
    border-radius: 18px;
    box-shadow: 0 6px 18px rgba(0,0,0,0.12);
    overflow: hidden;
  }

  /* Front side: portrait */
  .card--front {
    left: 90px; top: 194px;
    width: 340px; height: 612px;
  }
  .brand {
    position: absolute;
    left: 50%; top: 50%;
    transform: translate(-50%, -50%) rotate(90deg);
    display: flex; align-items: center; gap: 18px;
    white-space: nowrap;
  }
  .brand__dot {
    width: 22px; height: 22px; border-radius: 50%;
    background: var(--ink);
  }
  .brand__name {
    font-weight: 300;
    font-size: 40px;
    letter-spacing: 6px;
    text-transform: uppercase;
    color: var(--ink);
  }

  /* Back side: landscape */
  .card--back {
    left: 498px; top: 330px;
    width: 612px; height: 340px;
  }
  .person { position: absolute; left: 40px; top: 30px; }
  .person__name {
    font-size: 26px; font-weight: 400; color: var(--orange);
  }
  .person__role {
    margin-top: 4px;
    font-size: 17px; font-weight: 500; color: var(--grey-dark);
  }
  .divider {
    position: absolute; left: 40px; right: 40px; top: 104px;
    border-top: 2px dotted var(--rule);
  }
  .contacts {
    position: absolute; left: 40px; top: 114px;
    list-style: none;
  }
  .contacts li {
    display: flex; align-items: center; gap: 10px;
    font-size: 16px; font-weight: 300; color: var(--grey);
    line-height: 24px;
  }
  .contacts svg { width: 14px; height: 14px; fill: var(--orange); flex: none; }
  .band {
    position: absolute; left: 0; right: 0; top: 200px; height: 52px;
    background: var(--orange);
    display: flex; align-items: center; justify-content: space-between;
    padding: 0 40px;
  }
  .band__tagline {
    color: var(--card); font-size: 20px; font-weight: 300;
  }
  .band__brand {
    color: var(--card); font-size: 15px; font-weight: 300;
    letter-spacing: 2px; text-transform: uppercase;
  }
  .address {
    position: absolute; left: 40px; top: 266px;
    font-style: normal; font-size: 17px; font-weight: 300;
    color: var(--grey-dark); line-height: 24px;
  }
</style>
</head>
<body>
  <section class="card card--front" aria-label="Лицевая сторона">
    <div class="brand">
      <span class="brand__dot"></span>
      <span class="brand__name">Northern Herons</span>
    </div>
  </section>

  <section class="card card--back" aria-label="Оборотная сторона">
    <div class="person">
      <p class="person__name">Вера Ломакина</p>
      <p class="person__role">Управляющий партнёр</p>
    </div>
    <div class="divider"></div>
    <ul class="contacts">
      <li>
        <svg viewBox="0 0 16 16"><path d="M3.5 1l2.5 3-1.5 2c1 2 2.5 3.5 4.5 4.5l2-1.5 3 2.5-1.5 2.5C7 14 2 9 1 2.5z"/></svg>
        +7 (916) 507-28-14
      </li>
      <li>
        <svg viewBox="0 0 16 16"><path d="M1 3h14v10H1z M1 3l7 6 7-6" fill="none" stroke="#f29d12" stroke-width="1.6"/></svg>
        vera@northernherons.ru
      </li>
      <li>
        <svg viewBox="0 0 16 16"><circle cx="3" cy="13" r="2"/><path d="M1 7a8 8 0 0 1 8 8h-2a6 6 0 0 0-6-6z M1 2a13 13 0 0 1 13 13h-2A11 11 0 0 0 1 4z"/></svg>
        www.northernherons.ru
      </li>
    </ul>
    <div class="band">
      <span class="band__tagline">Брендинговое агентство</span>
      <span class="band__brand">Northern Herons</span>
    </div>
    <address class="address">
      115288, г. Москва<br>
      ул. Верескова, д.12, стр.5
    </address>
  </section>
</body>
</html>
```